Marova Hand Wash

Design hand washes. Total 12 variants to be designed.

Variants name are:

1) MILK &OLIVE
2) Shea Butter
3) Hidden Glow
4) Cream and Peach
5) Milk and Honey
6) Amber Riddle
7) Bakhour
8) Musk
9) White Oud
10) Black Oud
11) Rose Oud
12) Oud & Sandalwood

Labels can be on transparent sticker or background colors. All variants will be differentiated by fragrances and color. Bottle will be transparent. Pumps used for dispensing will be in Black or Transparent Color.

Designers can initially present designs of 4-5 variants initially. Later based on feedback, they can work out on more.

Bottle is 400ml and shape is rectangle. Ignore the size on bottle picture. Bottle keyline is attached.

Target Market(s)

B+, B, C+

Requirements
Must have
• Some relation to the variant names

```html
<!DOCTYPE html>
<html lang="en">
<head>
<meta charset="utf-8">
<title>Marova Peaches &amp; Cream Hand Wash Label</title>
<link href="https://fonts.googleapis.com/css2?family=Lobster&family=Montserrat:wght@500;600&display=swap" rel="stylesheet">
<style>
  :root {
    --page-bg: #ffffff;
    --label-yellow-deep: #ffcf4f;
    --label-yellow-mid: #ffe27a;
    --label-yellow-light: #fff6c2;
    --brand-purple: #6a5cae;
    --leaf-green: #3aa629;
    --title-red: #e8421a;
    --title-orange: #f26a1f;
    --ink-dark: #2a2320;
    --pill-orange: #f0561b;
    --pill-text: #fff4e8;
    --fruit-peach: #f49a5a;
    --fruit-yellow: #ffd45e;
    --splash-pink: #f6b3a8;
  }
  * { box-sizing: border-box; margin: 0; padding: 0; }
  html, body {
    width: 1200px;
    height: 1200px;
    overflow: hidden;
    background: var(--page-bg);
  }
  .label {
    position: absolute;
    left: 290px;
    top: 50px;
    width: 620px;
    height: 1100px;
    overflow: hidden;
    background:
      radial-gradient(ellipse at 50% 38%, var(--label-yellow-light) 0%, var(--label-yellow-mid) 45%, var(--label-yellow-deep) 100%);
  }
  .brand {
    position: absolute;
    top: 110px;
    left: 0;
    width: 100%;
    text-align: center;
  }
  .brand-name {
    font-family: "Montserrat", sans-serif;
    font-weight: 600;
    font-size: 92px;
    line-height: 1;
    color: var(--brand-purple);
    letter-spacing: -1px;
  }
  .brand-tagline {
    margin-top: 6px;
    font-family: "Montserrat", sans-serif;
    font-weight: 500;
    font-size: 18px;
    color: var(--brand-purple);
    padding-left: 200px;
  }
  .variant-kicker {
    position: absolute;
    top: 310px;
    left: 0;
    width: 100%;
    display: flex;
    justify-content: center;
    align-items: center;
    gap: 14px;
    font-family: "Lobster", cursive;
    font-size: 26px;
    color: var(--leaf-green);
  }
  .variant-kicker .rule {
    width: 58px;
    height: 2px;
    background: var(--leaf-green);
  }
  .variant-title {
    position: absolute;
    top: 345px;
    left: 0;
    width: 100%;
    font-family: "Lobster", cursive;
    color: var(--title-red);
    line-height: 0.9;
  }
  .variant-title .line-one {
    display: block;
    font-size: 128px;
    padding-left: 58px;
  }
  .variant-title .line-two {
    display: block;
    font-size: 128px;
    padding-left: 100px;
    color: var(--title-orange);
  }
  .product-type {
    position: absolute;
    top: 568px;
    right: 106px;
    font-family: "Montserrat", sans-serif;
    font-weight: 600;
    font-size: 28px;
    color: var(--ink-dark);
  }
  .fruit-art {
    position: absolute;
    left: 0;
    bottom: 0;
    width: 620px;
    height: 420px;
  }
  .volume-badge {
    position: absolute;
    left: 50%;
    top: 1018px;
    transform: translateX(-50%);
    width: 136px;
    height: 50px;
    border-radius: 25px;
    background: var(--pill-orange);
    color: var(--pill-text);
    font-family: "Montserrat", sans-serif;
    font-weight: 600;
    font-size: 26px;
    letter-spacing: 2px;
    display: flex;
    align-items: center;
    justify-content: center;
  }
</style>
</head>
<body>
  <div class="label">
    <div class="brand">
      <div class="brand-name">Marova</div>
      <div class="brand-tagline">Air Freshener</div>
    </div>

    <div class="variant-kicker">
      <span class="rule"></span><span>Pure</span><span class="rule"></span>
    </div>

    <div class="variant-title">
      <span class="line-one">Peaches</span>
      <span class="line-two">&amp; Cream</span>
    </div>
    <div class="product-type">HAND WASH</div>

    <svg class="fruit-art" viewBox="0 0 620 420" role="img" aria-label="Ripe peaches with a halved peach and green leaves splashing into pink cream">
      <defs>
        <radialGradient id="fruitGlow" cx="50%" cy="40%" r="60%">
          <stop offset="0%" stop-color="var(--fruit-yellow)"/>
          <stop offset="55%" stop-color="var(--fruit-peach)"/>
          <stop offset="100%" stop-color="var(--splash-pink)"/>
        </radialGradient>
      </defs>
      <path d="M0 160 Q150 20 320 40 Q500 60 620 140 L620 420 L0 420 Z" fill="url(#fruitGlow)"/>
    </svg>

    <div class="volume-badge">400ML</div>
  </div>
</body>
</html>
```